Tervolan Pty Ltd professional business card

A professional business card template using the colours from the supplied logo.
Clean crisp lines while, Modern while not being over the top.

Target Market(s)

Construction, commerical and industrial

Industry/Entity Type

Communications

Contact Information for Business Card

For a Communications, IT, Optical fibre installation company

Colors
37b8a4

```html
<!DOCTYPE html>
<html lang="en">
<head>
<meta charset="UTF-8">
<title>Tervolan Pty Ltd – Business Card</title>
<link rel="stylesheet" href="https://fonts.googleapis.com/css2?family=Poppins:wght@400;500;600&display=swap">
<style>
  :root {
    --backdrop: #2b2c2e;
    --teal: #1794a5;
    --teal-deep: #138e9f;
    --teal-muted: #4a8a92;
    --ink: #6b6c70;
    --paper: #ffffff;
    --paper-shade: #eef2f4;
  }
  * { margin: 0; padding: 0; box-sizing: border-box; }
  html, body {
    width: 1200px; height: 900px; overflow: hidden;
    background: var(--backdrop);
    font-family: "Poppins", sans-serif;
  }
  .stage { position: relative; width: 1200px; height: 900px; }
  .card {
    position: absolute; left: 250px; width: 700px; height: 400px;
    overflow: hidden;
    box-shadow: 0 10px 30px rgba(0,0,0,.45);
  }
  .card-front {
    top: 35px;
    background: linear-gradient(25deg, var(--paper-shade) 0%, var(--paper) 45%);
  }
  .card-back {
    top: 465px;
    background: linear-gradient(110deg, var(--teal-muted) 0%, var(--teal-deep) 70%, var(--teal) 100%);
  }
  .wordmark {
    position: absolute; left: 95px; top: 58px;
    font-size: 58px; line-height: 70px; font-weight: 600; letter-spacing: 2px;
    color: var(--ink); white-space: nowrap;
  }
  .rule { position: absolute; left: 0; top: 0; }
  .contact-list {
    position: absolute; left: 70px; top: 238px;
    list-style: none; color: var(--ink); font-size: 15px; line-height: 24px;
  }
  .contact-list li { display: flex; align-items: center; gap: 10px; }
  .contact-list svg { width: 14px; height: 14px; flex: none; }
  .person { position: absolute; right: 72px; top: 160px; text-align: left; }
  .person-name {
    display: inline-block; background: var(--teal); color: var(--paper);
    font-size: 18px; font-weight: 600; letter-spacing: .5px;
    padding: 1px 12px; line-height: 28px; white-space: nowrap;
  }
  .person-role { color: var(--ink); font-size: 14px; line-height: 20px; margin-top: 3px; padding-left: 4px; }
  .edge-tab { position: absolute; right: 0; top: 200px; width: 20px; height: 22px; background: var(--teal); }
  .address {
    position: absolute; right: 70px; top: 278px;
    text-align: right; color: var(--ink); font-size: 15px; line-height: 24px; font-style: normal;
  }
  .back-wordmark {
    position: absolute; left: 0; right: 0; top: 140px; text-align: center;
    font-size: 70px; font-weight: 600; letter-spacing: 3px; color: var(--paper);
  }
  .back-web {
    position: absolute; left: 0; right: 0; top: 270px; text-align: center;
    font-size: 16px; color: var(--paper); letter-spacing: .5px;
  }
</style>
</head>
<body>
<main class="stage">
  <section class="card card-front" aria-label="Card front">
    <div class="wordmark">TERVOLAN</div>

    <svg class="rule" width="700" height="400" viewBox="0 0 700 400" aria-hidden="true">
      <path d="M70 222 H380 L390 228 H410 L420 232 H540" fill="none" stroke="var(--teal)" stroke-width="1.5"/>
      <path d="M430 266 H640" fill="none" stroke="var(--teal)" stroke-width="1.5"/>
    </svg>

    <ul class="contact-list">
      <li>
        <svg viewBox="0 0 16 16"><path d="M4 1 L6.5 4 L5 6 Q6.5 9.5 10 11 L12 9.5 L15 12 L13 15 Q3 13 1 3 Z" fill="var(--teal)"/></svg>
        555-318-0472
      </li>
      <li>
        <svg viewBox="0 0 16 16"><rect x="1" y="3" width="14" height="10" fill="var(--teal)"/><path d="M1 3 L8 9 L15 3" fill="none" stroke="#fff" stroke-width="1.2"/></svg>
        dana@tervolan.com.au
      </li>
      <li>
        <svg viewBox="0 0 16 16"><circle cx="8" cy="8" r="6.5" fill="none" stroke="var(--teal)" stroke-width="1.4"/><path d="M1.5 8 H14.5 M8 1.5 V14.5 M8 1.5 Q3.5 8 8 14.5 M8 1.5 Q12.5 8 8 14.5" fill="none" stroke="var(--teal)" stroke-width="1"/></svg>
        www.tervolan.com.au
      </li>
    </ul>

    <div class="person">
      <div class="person-name">DANA WHITLOW</div>
      <div class="person-role">CEO/FOUNDER</div>
    </div>
    <div class="edge-tab"></div>

    <address class="address">
      118 Harlow Street NW<br>
      Suite 210, Fernvale<br>
      MI 49120
    </address>
  </section>

  <section class="card card-back" aria-label="Card back">
    <div class="back-wordmark">TERVOLAN</div>
    <div class="back-web">www.tervolan.com.au</div>
  </section>
</main>
</body>
</html>
```